Carpentry and Building Business Card

I'm looking for a business card that is minimalistic and that incorporates the theme of my Velmor logo.
On one side I'd like the VELMOR logo with my details on the other side.
Double sided with curved edges

Target Market(s)

Construction / renovation
Adults

Industry/Entity Type

Tradesman

Contact Information for Business Card

Logo on one side, details on the other

Colors

Designer to choose only greyscale colors for use in the design.

Requirements
Must have
• Nilo Petrakis
VELMOR CONSTRUCT
Carpentry & Building Services
0481236574
Velmorconstruct@brixmail.com
Lic No. 718263D
Nice to have
• Fb and insta icons. @velmorconstruct
Should not have
• No hammer or tool icons please.

No address line.

```html
<!DOCTYPE html>
<html lang="en">
<head>
<meta charset="utf-8">
<title>Velmor Construct Business Card</title>
<link rel="stylesheet" href="https://fonts.googleapis.com/css2?family=Tinos:wght@400&display=swap">
<style>
  :root {
    --canvas: #3a3839;
    --card-white: #ffffff;
    --card-grey: #c9c9c9;
    --pattern-grey: #d6d6d6;
    --ink: #111111;
    --ink-soft: #6e6e6e;
    --rule: #9a9a9a;
    --mark: #7a7a7a;
  }
  * { box-sizing: border-box; margin: 0; padding: 0; }
  html, body { width: 1200px; height: 900px; overflow: hidden; }
  body {
    background: var(--canvas);
    font-family: "Tinos", "Times New Roman", serif;
    color: var(--ink);
    position: relative;
  }
  .card {
    position: absolute;
    left: 290px;
    width: 620px;
    height: 354px;
    border-radius: 30px;
    overflow: hidden;
  }
  .card--details { top: 64px; background: var(--card-white); }
  .card--brand { top: 482px; background: var(--card-grey); }

  /* details side */
  .brand-block {
    position: absolute; left: 30px; top: 44px; width: 260px;
    text-align: center;
  }
  .brand-mark {
    width: 110px; height: 110px; margin: 0 auto 22px;
    border: 5px solid var(--mark);
  }
  .brand-name { font-size: 25px; letter-spacing: 0.5px; color: var(--ink); }
  .brand-tagline {
    margin-top: 4px; font-size: 15px; color: var(--ink-soft);
    display: flex; align-items: center; justify-content: center; gap: 4px;
  }
  .brand-tagline::before, .brand-tagline::after {
    content: ""; width: 14px; height: 1px; background: var(--ink-soft);
  }
  .top-rule {
    position: absolute; left: 0; top: 236px; width: 30px; height: 2px; background: var(--rule);
  }
  .divider {
    position: absolute; left: 312px; top: 112px; width: 2px; height: 160px; background: var(--rule);
  }
  .contact-block { position: absolute; left: 336px; top: 104px; }
  .person-name { font-size: 38px; line-height: 1; margin-bottom: 16px; }
  .person-name .surname { color: var(--ink-soft); }
  .contact-list { list-style: none; }
  .contact-list li {
    display: flex; align-items: center; gap: 10px;
    font-size: 19px; line-height: 1; margin-bottom: 10px;
  }
  .contact-list svg { width: 16px; height: 16px; flex: none; }
  .licence-row {
    position: absolute; left: 0; right: 0; bottom: 26px;
    display: flex; align-items: center; gap: 14px;
  }
  .licence-row::before { content: ""; flex: 1; height: 2px; background: var(--rule); }
  .licence-row::after { content: ""; width: 90px; height: 2px; background: var(--rule); }
  .licence { font-size: 24px; }

  /* brand side */
  .brand-pattern { position: absolute; inset: 0; background: linear-gradient(135deg, var(--pattern-grey), var(--card-grey)); }
  .brand-lockup {
    position: absolute; left: 50%; top: 50%; transform: translate(-50%, -50%);
    display: flex; align-items: center; gap: 12px;
  }
  .brand-lockup .brand-mark-small { width: 44px; height: 44px; background: var(--card-white); }
  .brand-lockup .brand-name { font-size: 22px; }
</style>
</head>
<body>
  <section class="card card--details">
    <div class="brand-block">
      <div class="brand-mark"></div>
      <p class="brand-name">VELMOR CONSTRUCT</p>
      <p class="brand-tagline">Carpentry &amp; Building Services</p>
    </div>
    <div class="top-rule"></div>
    <div class="divider"></div>
    <div class="contact-block">
      <p class="person-name">Nilo <span class="surname">Petrakis</span></p>
      <ul class="contact-list">
        <li>
          <svg viewBox="0 0 16 16" aria-hidden="true"><path d="M3 1.5h3l1.2 3.3-1.8 1.2a8 8 0 0 0 4.6 4.6l1.2-1.8 3.3 1.2v3a1.5 1.5 0 0 1-1.6 1.5A12.5 12.5 0 0 1 1.5 3.1 1.5 1.5 0 0 1 3 1.5z" fill="#444"/></svg>
          0481236574
        </li>
        <li>
          <svg viewBox="0 0 16 16" aria-hidden="true"><rect x="1" y="3" width="14" height="10" fill="none" stroke="#444" stroke-width="1.4"/><path d="M1 3l7 6 7-6" fill="none" stroke="#444" stroke-width="1.4"/></svg>
          Velmorconstruct@brixmail.com
        </li>
        <li>
          <svg viewBox="0 0 16 16" aria-hidden="true"><rect x="2" y="2" width="12" height="12" fill="#444"/></svg>
          @velmorconstruct
        </li>
        <li>
          <svg viewBox="0 0 16 16" aria-hidden="true"><circle cx="8" cy="8" r="6" fill="#444"/></svg>
          @velmorconstruct
        </li>
      </ul>
    </div>
    <div class="licence-row"><span class="licence">Lic No. 718263D</span></div>
  </section>

  <section class="card card--brand">
    <div class="brand-pattern" role="img" aria-label="Faint repeating brand pattern in light grey"></div>
    <div class="brand-lockup">
      <div class="brand-mark-small"></div>
      <p class="brand-name">VELMOR CONSTRUCT</p>
    </div>
  </section>
</body>
</html>
```